General Dental Office Business Card

I run a private general dental office in southern California, and would like a refresh/redesign of my business card. I focus on quality care rather than volume. The email address on the uploaded current card should be updated to: info@marbleshoredental.example. The current card's logo is a deboss, but I am open to other ideas. The logo can be refreshed, but it is something that's been with me since the beginning of the office, so I wouldn't want a drastic redesign.
Target Market(s)
Adults 18-99, whoever needs dental services
Industry/Entity Type
Healthcare/Dental
Contact Information for Business Card
Name, Address, Phone, email
Colors
Designer to choose colors to be used in the design.
Requirements
Must have
- Logo (Same as original one in the uploaded file), space on back for appointment time/date

```html
<!DOCTYPE html>
<html lang="en">
<head>
<meta charset="utf-8">
<title>Marble Shore Dental – Business Card</title>
<link rel="stylesheet" href="https://fonts.googleapis.com/css2?family=Montserrat:wght@600;700&family=Mulish:wght@400;500&display=swap">
<style>
  :root {
    --backdrop: #d3d3cf;
    --paper: #ffffff;
    --charcoal: #333333;
    --sky: #7fd0e6;
    --sky-deep: #1fa9d6;
    --ink: #3a3a3a;
    --title-blue: #5fb3cc;
  }
  * { box-sizing: border-box; margin: 0; padding: 0; }
  html, body { width: 1200px; height: 801px; overflow: hidden; }
  body {
    background: var(--backdrop);
    font-family: "Mulish", "Helvetica Neue", Arial, sans-serif;
    position: relative;
  }
  .card {
    position: absolute;
    top: 246px;
    width: 540px;
    height: 309px;
    border-bottom: 4px solid var(--sky);
    box-shadow: 0 10px 24px rgba(0,0,0,0.18);
    overflow: hidden;
  }
  /* Front */
  .card--front { left: 40px; background: var(--paper); color: var(--ink); }
  .brand {
    position: absolute; left: 36px; top: 34px;
    display: flex; align-items: center; gap: 14px;
  }
  .brand__dot { width: 64px; height: 64px; border-radius: 50%; background: var(--sky); }
  .brand__name {
    font-family: "Montserrat", sans-serif; font-weight: 600;
    font-size: 20px; color: var(--sky); letter-spacing: 0.5px;
  }
  .identity { position: absolute; left: 36px; top: 122px; }
  .identity__name {
    font-family: "Montserrat", sans-serif; font-weight: 700;
    font-size: 21px; color: var(--sky); letter-spacing: 0.6px;
  }
  .identity__role { font-size: 15px; margin-top: 2px; }
  .contact { list-style: none; margin-top: 10px; font-size: 14px; line-height: 21px; }
  .contact li { display: flex; align-items: center; gap: 8px; }
  .contact svg { width: 12px; height: 12px; flex: none; }
  .contact .web-accent { color: var(--sky-deep); }
  .divider {
    position: absolute; left: 36px; right: 36px; top: 258px;
    height: 1px; background: var(--sky-deep);
  }
  .address { position: absolute; left: 36px; top: 268px; font-size: 14px; }

  /* Back */
  .card--back { left: 620px; background: var(--charcoal); color: #f2f2f2; }
  .back__title {
    position: absolute; left: 30px; top: 24px;
    font-family: "Montserrat", sans-serif; font-weight: 700;
    font-size: 24px; color: var(--title-blue); letter-spacing: 1px;
  }
  .fields { position: absolute; left: 30px; top: 72px; right: 30px; font-size: 13px; }
  .field { display: flex; align-items: flex-end; gap: 6px; height: 22px; }
  .field__label { white-space: nowrap; }
  .field__line { flex: 1; border-bottom: 1.5px dotted var(--sky); margin-bottom: 4px; }
  .field--name .field__label { color: #b8b8b8; }
  .field--gap { margin-top: 12px; }
  .days {
    position: absolute; left: 30px; top: 214px;
    display: flex; gap: 18px; font-size: 14px;
  }
  .day { display: flex; align-items: center; gap: 4px; }
  .day__box { width: 10px; height: 10px; border: 1.5px solid var(--sky); }
  .wave-band {
    position: absolute; left: 0; right: 0; bottom: 0; height: 58px;
    background: linear-gradient(180deg, var(--charcoal) 0%, #4d7d8b 100%);
  }
</style>
</head>
<body>

<section class="card card--front" aria-label="Business card front">
  <div class="brand">
    <span class="brand__dot"></span>
    <span class="brand__name">Marble Shore Dental</span>
  </div>
  <div class="identity">
    <h1 class="identity__name">DANIEL R. MOREAU DDS</h1>
    <p class="identity__role">General Dentistry</p>
    <ul class="contact">
      <li><svg viewBox="0 0 12 12"><path d="M2.5 1l2 2.3-1 1.2a6 6 0 0 0 4 4l1.2-1 2.3 2-1.2 1.5C5 11 1 7 1 2.2z" fill="var(--sky-deep)"/></svg><span>949-555-0142</span></li>
      <li><svg viewBox="0 0 12 12"><rect x="1" y="2.5" width="10" height="7" fill="none" stroke="var(--sky-deep)" stroke-width="1.2"/><path d="M1 2.5l5 4 5-4" fill="none" stroke="var(--sky-deep)" stroke-width="1.2"/></svg><span>info@marbleshoredental.example</span></li>
      <li><svg viewBox="0 0 12 12"><circle cx="6" cy="6" r="5" fill="var(--sky-deep)"/><path d="M1 6h10M6 1c-2 2.5-2 7.5 0 10M6 1c2 2.5 2 7.5 0 10" stroke="#fff" stroke-width="0.8" fill="none"/></svg><span>www.<span class="web-accent">marbleshoredental</span>.example</span></li>
    </ul>
  </div>
  <div class="divider"></div>
  <p class="address">2180 Coral Crest Parkway Marble Shore, CA 92600</p>
</section>

<section class="card card--back" aria-label="Business card back, appointment reminder">
  <h2 class="back__title">MARBLE SHORE DENTAL</h2>
  <div class="fields">
    <div class="field field--name"><span class="field__label">Patient Name :</span><span class="field__line"></span></div>
    <div class="field field--gap"><span class="field__label">Appointment Date</span><span class="field__line"></span></div>
    <div class="field"><span class="field__label">Appointment Date</span><span class="field__line"></span></div>
    <div class="field field--gap"><span class="field__label">Time</span><span class="field__line"></span><span class="field__label">am / pm</span></div>
    <div class="field"><span class="field__label">Time</span><span class="field__line"></span><span class="field__label">am / pm</span></div>
  </div>
  <div class="days">
    <span class="day">Sun<span class="day__box"></span></span>
    <span class="day">Mon<span class="day__box"></span></span>
    <span class="day">Tue<span class="day__box"></span></span>
    <span class="day">Wed<span class="day__box"></span></span>
    <span class="day">Thu<span class="day__box"></span></span>
    <span class="day">Fri<span class="day__box"></span></span>
    <span class="day">Sat<span class="day__box"></span></span>
  </div>
  <div class="wave-band" role="img" aria-label="Decorative wavy sky-blue stripe band along the bottom edge"></div>
</section>

</body>
</html>
```